Substance abuse awareness flyer for school age kids

I am needing a flyer for school-age kids. What if it were designed to look like an Voxtab with someone texting and the text bubbles were some of the text below with emojis? Maybe a text chain between to friends:

Maybe the first text bubble says "I'm thinking about using drugs and alcohol"
the next bubble: "Just say no!" ( perhaps a stop sign emoji ?)

"Talk to your parents, your teachers at school, or your doctor about how drugs and alcohol can harm you"

another text bubble "did you know that alcohol and drugs could lead to..."
then include some of the info below (see links for more info).
Where ever you get info, it must be cited.

this needs to be English on one side and Spanish on the other side and needs to include the logo attached.

The effects of substance abuse
BHW: https://www.bhwagency.org/youth/features/teen-substance-use.html
Affect growth and development, especially brain development. Not able to focus at school or be around friends. https://www.kestrowline.org/sites/default/files/preventingdruguse_2.pdf
Leads to risky behaviors and lack of impulse control (dangerous activities) https://www.kestrowline.org/sites/default/files/preventingdruguse_2.pdf
Contribute to health problems as an adult: heart disease, high blood pressure, and trouble sleeping.

Target Market(s)

school age kids 9-20

Requirements
Must have
• Print ready: 8.5x11

```html
<!DOCTYPE html>
<html lang="en">
<head>
<meta charset="utf-8">
<title>The Effects of Substance Abuse – Flyer</title>
<link href="https://fonts.googleapis.com/css2?family=Bebas+Neue&family=Lato:wght@400;700&display=swap" rel="stylesheet">
<style>
  :root {
    --backdrop: #1c1819;
    --white: #ffffff;
    --magenta: #d63fd6;
    --violet: #b95ae6;
    --blue: #5b6cf0;
    --blue-soft: #7d8cf5;
    --peach: #f1d9c2;
    --pink: #e48fc9;
    --ink: #3b3f52;
    --chat-bg: #e9ecff;
    --link-bg: #e6e7ee;
    --phone-frame: #f4f4f6;
  }
  * { box-sizing: border-box; margin: 0; padding: 0; }
  html, body { width: 1200px; height: 1200px; overflow: hidden; }
  body { background: var(--backdrop); font-family: 'Lato', sans-serif; position: relative; }

  .flyer {
    position: absolute; left: 188px; top: 68px;
    width: 824px; height: 1064px;
    background: var(--white); overflow: hidden;
  }
  .hero-photo {
    position: absolute; left: 0; top: 100px; width: 824px; height: 940px;
    background:
      radial-gradient(ellipse 55% 50% at 50% 48%, var(--peach) 0%, rgba(241,217,194,0.85) 45%, rgba(241,217,194,0) 100%),
      linear-gradient(180deg, var(--pink) 0%, #d67fd3 60%, var(--magenta) 100%);
  }
  .title-band { position: absolute; left: 0; top: 0; width: 824px; height: 100px; background: var(--white); }
  .title {
    position: absolute; left: 220px; top: 26px;
    font-family: 'Bebas Neue', sans-serif; font-weight: 400; font-size: 54px; letter-spacing: 0.5px; line-height: 1;
    color: var(--magenta);
  }
  .title .accent { color: var(--blue); }
  .title-rule { position: absolute; left: 483px; top: 79px; width: 341px; height: 3px; background: var(--violet); }

  .brand-badge {
    position: absolute; left: 22px; top: 20px; width: 168px; height: 168px;
    border-radius: 50%; background: var(--white);
    border: 4px solid var(--blue-soft);
    box-shadow: 0 0 0 6px var(--white), 0 0 0 12px var(--blue);
    display: flex; align-items: center; justify-content: center; text-align: center;
  }
  .brand-name {
    font-family: 'Lato', sans-serif; font-weight: 700; font-size: 19px; line-height: 1.15;
    color: var(--blue); text-transform: uppercase; letter-spacing: 1px;
  }

  .phone {
    position: absolute; left: 224px; top: 131px; width: 395px; height: 853px;
    background: var(--phone-frame); border-radius: 56px;
    box-shadow: 0 6px 24px rgba(90,40,90,0.25);
  }
  .phone-speaker { position: absolute; left: 166px; top: 60px; width: 64px; height: 6px; border-radius: 3px; background: #2b2b2e; }
  .phone-camera { position: absolute; left: 191px; top: 22px; width: 12px; height: 12px; border-radius: 50%; background: #2b2b2e; }
  .phone-button { position: absolute; left: 170px; top: 787px; width: 56px; height: 56px; border-radius: 50%; border: 2px solid #dcdce0; }

  .screen {
    position: absolute; left: 17px; top: 94px; width: 362px; height: 671px;
    background: var(--chat-bg); border: 1px solid var(--blue-soft);
    display: flex; flex-direction: column; overflow: hidden;
  }
  .chat-header {
    height: 61px; flex-shrink: 0; background: var(--blue); display: flex; align-items: center;
    padding: 0 14px; color: var(--white);
  }
  .avatar { width: 46px; height: 46px; border-radius: 50%; background: #b98566; border: 2px solid var(--white); }
  .contact-name { font-size: 20px; margin-left: 12px; flex: 1; }
  .chat-actions { display: flex; align-items: center; gap: 12px; }

  .thread { display: flex; flex-direction: column; gap: 8px; padding: 12px 12px 0 12px; }
  .bubble {
    font-size: 13.5px; line-height: 1.25; padding: 5px 12px; border-radius: 16px;
  }
  .bubble.sent {
    align-self: flex-end; background: var(--blue); color: var(--white);
    border-top-right-radius: 3px; white-space: nowrap;
  }
  .bubble.received {
    align-self: flex-start; background: var(--white); color: var(--ink); width: 292px;
    border-top-left-radius: 3px; box-shadow: 0 1px 3px rgba(0,0,0,0.12);
    padding: 7px 14px 8px;
  }
  .bubble.received.short { width: auto; }
  .bubble p + p, .bubble p + .source, .bubble .source + p { margin-top: 10px; }
  .source { display: block; background: var(--link-bg); padding: 2px 6px; font-size: 13px; overflow-wrap: anywhere; margin-left: -6px; }

  .footer-rule { position: absolute; left: 0; top: 1040px; width: 824px; height: 24px; background: var(--blue); }
  .footer-line { position: absolute; left: 0; top: 1026px; width: 824px; height: 14px; background: var(--blue-soft); }
  .web-tab {
    position: absolute; left: 0; top: 1012px; width: 404px; height: 56px;
    background: var(--white); border-top-right-radius: 40px;
    display: flex; align-items: center; padding-left: 32px; gap: 8px;
  }
  .web-tab svg { flex-shrink: 0; }
  .web-address { font-weight: 700; font-size: 25px; color: var(--blue); white-space: nowrap; }
  .social { position: absolute; right: 16px; top: 952px; display: flex; gap: 6px; }
  .social span { width: 40px; height: 40px; border-radius: 50%; background: var(--white); display: block; }
</style>
</head>
<body>
  <main class="flyer">
    <div class="hero-photo" role="img" aria-label="Photo of a hand holding a smartphone over scattered pills and capsules"></div>

    <header class="title-band">
      <h1 class="title">The Effects of <span class="accent">Substance Abuse</span></h1>
      <div class="title-rule"></div>
    </header>

    <div class="brand-badge">
      <span class="brand-name">Riverbend<br>Health<br>Systems</span>
    </div>

    <div class="phone">
      <div class="phone-camera"></div>
      <div class="phone-speaker"></div>
      <section class="screen">
        <div class="chat-header">
          <div class="avatar" role="img" aria-label="Profile photo of the best friend"></div>
          <span class="contact-name">Best Friend</span>
          <div class="chat-actions">
            <svg width="28" height="18" viewBox="0 0 28 18" aria-hidden="true"><rect x="0" y="2" width="19" height="14" rx="2" fill="#fff"/><path d="M20 9 L28 3 V15 Z" fill="#fff"/></svg>
            <svg width="20" height="20" viewBox="0 0 24 24" aria-hidden="true"><path fill="#fff" d="M6.6 10.8a15.1 15.1 0 0 0 6.6 6.6l2.2-2.2c.3-.3.7-.4 1-.2 1.1.4 2.3.6 3.6.6.6 0 1 .4 1 1V20c0 .6-.4 1-1 1C10.6 21 3 13.4 3 4c0-.6.4-1 1-1h3.5c.6 0 1 .4 1 1 0 1.3.2 2.5.6 3.6.1.3 0 .7-.2 1z"/></svg>
            <svg width="6" height="20" viewBox="0 0 6 20" aria-hidden="true"><circle cx="3" cy="3" r="2.4" fill="#fff"/><circle cx="3" cy="10" r="2.4" fill="#fff"/><circle cx="3" cy="17" r="2.4" fill="#fff"/></svg>
          </div>
        </div>

        <div class="thread">
          <div class="bubble sent">Hey.. I'm thinking about using drugs or alcohol...</div>
          <div class="bubble received short">Whattt?! NOOO!!!! &nbsp;🙅‍♀️👎❌</div>
          <div class="bubble received">
            <p>Did you know that alcohol &amp; drugs could affect growth and development, especially brain development. Not able to focus at school or be around friends..</p>
            <span class="source">https://www.bhwagency.org/youth/<wbr>features/teen-substance-use.html</span>
          </div>
          <div class="bubble sent">Sounds scary..... 😧</div>
          <div class="bubble received">
            <p>YEA!! It also leads to risky behaviors &amp; lack of impulse control (dangerous activities)</p>
            <span class="source">https://www.kestrowline.org/sites/default/<wbr>files/preventingdruguse_2.pdf</span>
            <p>Also it Contribute to health problems as an adult: heart disease, high blood pressure, and trouble sleeping.</p>
            <span class="source">https://www.kestrowline.org/sites/default/<wbr>files/preventingdruguse_2.pdf</span>
          </div>
          <div class="bubble received">Talk to your parents, your teachers at school, or your doctor about how drugs &amp; alcohol can harm you"</div>
          <div class="bubble sent">I will.... Thanks, dear... ❤️</div>
        </div>
      </section>
      <div class="phone-button"></div>
    </div>

    <div class="social" aria-label="Social media links">
      <span></span><span></span>
    </div>

    <div class="footer-line"></div>
    <div class="footer-rule"></div>
    <div class="web-tab">
      <svg width="24" height="24" viewBox="0 0 24 24" aria-hidden="true" fill="none" stroke="#d63fd6" stroke-width="2"><circle cx="12" cy="12" r="10"/><ellipse cx="12" cy="12" rx="4.5" ry="10"/><line x1="2" y1="12" x2="22" y2="12"/></svg>
      <span class="web-address">www.riverbendhealth.org</span>
    </div>
  </main>
</body>
</html>
```